Young Accounting firm needing a captivating business card

We need a business card design that forces the person to look at the card because its either gold foil, plastic, or lettering pop up etc. We already have a logo with a specific gold color and we need to make it pop. We are an accounting firm. I need the words" accounting, payroll, licenses, audits, taxes" somewhere on the business card so as to describe what we do- preferably on the side where the logo is at.

Industry/Entity Type

Accounting

Contact Information for Business Card

Address 48276 9th Ave S Ste 305, Federal Way, WA 98117
Business Phone (360)418-2096
Fax (360)418-2157
Office Cell Phone (360)586-7319

Font styles to use
Serif

Colors
85abd2

Requirements
Must have
• It should state
• "Accounting" "Taxes" "Audits" "Licenses" "Payroll"
Nice to have
• Matte with gold foil, different textures, With Either a textured ivory background or gray blue slate background
Should not have
• colorful colors

```html
<!DOCTYPE html>
<html lang="en">
<head>
<meta charset="utf-8">
<title>Norvelle Ledger – Business Card</title>
<link rel="stylesheet" href="https://fonts.googleapis.com/css2?family=Crimson+Text:wght@400;600&display=swap">
<style>
  :root {
    --backdrop: #cfcfcf;
    --card: #07090c;
    --gold: #bb9a31;
    --ink-light: #f4f4f4;
    --ink-dark: #0b0b0b;
    --text-font: "Crimson Text", Georgia, serif;
  }
  * { box-sizing: border-box; margin: 0; padding: 0; }
  html, body {
    width: 1125px; height: 1200px; overflow: hidden;
    background: var(--backdrop);
    font-family: var(--text-font);
  }
  .canvas { position: relative; width: 1125px; height: 1200px; }

  .card {
    position: absolute; left: 172px; width: 780px; height: 443px;
    background: var(--card); border-radius: 26px; overflow: hidden;
  }
  .card--front { top: 122px; }
  .card--back { top: 636px; }

  /* Front */
  .brand {
    position: absolute; display: flex; align-items: center;
    color: var(--gold); font-weight: 600; white-space: nowrap;
  }
  .brand__mark { background: var(--gold); flex: none; }
  .card--front .brand {
    left: 40px; top: 196px; width: 320px; justify-content: center;
    font-size: 33px; gap: 12px;
  }
  .card--front .brand__mark { width: 22px; height: 22px; }

  .divider {
    position: absolute; left: 390px; top: 159px; width: 2px; height: 126px;
    background: var(--gold);
  }
  .contact-list {
    position: absolute; left: 428px; top: 156px; list-style: none;
    color: var(--ink-light); font-size: 19.5px; line-height: 26.2px;
  }
  .contact-list li { display: flex; align-items: center; gap: 11px; }
  .contact-list svg { width: 14px; height: 14px; fill: var(--gold); flex: none; }

  .address-band {
    position: absolute; left: 0; top: 383px; width: 100%; height: 33px;
    background: var(--gold); color: var(--ink-dark);
    display: flex; align-items: center; justify-content: center; gap: 9px;
    font-size: 19.5px;
  }
  .address-band svg { width: 20px; height: 20px; fill: var(--ink-dark); }

  /* Back */
  .card--back .brand {
    left: 0; top: 200px; width: 100%; flex-direction: column; gap: 18px;
    font-size: 54px; line-height: 1;
  }
  .card--back .brand__mark { width: 40px; height: 40px; }

  .services {
    position: absolute; left: 0; top: 372px; width: 100%;
    display: flex; justify-content: center; gap: 24px; list-style: none;
    color: var(--ink-light); font-size: 19.5px;
  }
  .services li { display: flex; align-items: center; gap: 13px; }
  .services li::before {
    content: ""; width: 7px; height: 7px; border-radius: 50%; background: var(--gold);
  }
</style>
</head>
<body>
<main class="canvas">

  <section class="card card--front" aria-label="Business card front">
    <div class="brand"><span class="brand__mark"></span>Norvelle Ledger</div>
    <div class="divider"></div>
    <ul class="contact-list">
      <li>
        <svg viewBox="0 0 16 16" aria-hidden="true"><path d="M3.6 1.2l2.3 2.6-1.3 1.7c.9 2 2.4 3.6 4.4 4.6l1.7-1.3 2.6 2.3-1.4 2.4C6.7 13.5 2.5 9.3 1.2 3z"/></svg>
        (360)586-7319
      </li>
      <li>
        <svg viewBox="0 0 16 16" aria-hidden="true"><path d="M4.5 0h7a1 1 0 0 1 1 1v14a1 1 0 0 1-1 1h-7a1 1 0 0 1-1-1V1a1 1 0 0 1 1-1zm.6 2v10h5.8V2zm2.9 11a1 1 0 1 0 0 2 1 1 0 0 0 0-2z"/></svg>
        (360)418-2096
      </li>
      <li>
        <svg viewBox="0 0 16 16" aria-hidden="true"><path d="M4 1h8v4H4zM1 6h14v6h-2.5v-2h-9v2H1zm3.5 5h7v4h-7z"/></svg>
        (360)418-2157
      </li>
      <li>
        <svg viewBox="0 0 16 16" aria-hidden="true"><path d="M1 3h14v10H1zm2 2v6h10V5l-5 4z"/></svg>
        info@norvelleledger.com
      </li>
      <li>
        <svg viewBox="0 0 16 16" aria-hidden="true"><path d="M8 0a8 8 0 1 0 0 16A8 8 0 0 0 8 0zm-3 3.5l2 1-.5 2 2 1.5-1 3-2-1.5-1-3zm6 1.5l1.5 2-1 3.5-2 1 .5-3-1.5-1.5z"/></svg>
        www.norvelleledger.com
      </li>
    </ul>
    <div class="address-band">
      <svg viewBox="0 0 20 20" aria-hidden="true"><path d="M10 1a5 5 0 0 0-5 5c0 3.5 5 9 5 9s5-5.5 5-9a5 5 0 0 0-5-5zm0 3a2 2 0 1 1 0 4 2 2 0 0 1 0-4zM3 15c0 2 3 3.5 7 3.5s7-1.5 7-3.5c0-1-1-1.8-2.6-2.4l-.6 1c1 .4 1.7.9 1.7 1.4 0 1.2-2.5 2.2-5.5 2.2s-5.5-1-5.5-2.2c0-.5.7-1 1.7-1.4l-.6-1C4 13.2 3 14 3 15z"/></svg>
      48276 9th Ave S Ste 305, Federal Way, WA 98117
    </div>
  </section>

  <section class="card card--back" aria-label="Business card back">
    <div class="brand"><span class="brand__mark"></span>Norvelle Ledger</div>
    <ul class="services">
      <li>Accounting</li>
      <li>Payroll</li>
      <li>Licenses</li>
      <li>Audits</li>
      <li>Taxes</li>
    </ul>
  </section>

</main>
</body>
</html>
```